TalkWell needs a Letterhead

We need a letterhead for our company "TalkWell Consultants". Logo is attached. The company color is Turquoise. Icons for website, scan logo for website, icons for address, e-mail and phone appreciated rather than just words.

```html
<!DOCTYPE html>
<html lang="en">
<head>
<meta charset="utf-8">
<title>TalkWell Consultants Letterhead</title>
<link rel="stylesheet" href="https://fonts.googleapis.com/css2?family=Open+Sans:wght@400;600&family=Tinos:wght@400;700&display=swap">
<style>
  :root {
    --brand-blue: #3d84c4;
    --brand-green: #8cc152;
    --accent-turquoise: #2a9bb0;
    --pale-blue: #d3e3ee;
    --text-body: #4a4a4a;
    --text-dark: #222222;
    --paper: #ffffff;
  }
  * { margin: 0; padding: 0; box-sizing: border-box; }
  html, body { width: 942px; height: 1200px; overflow: hidden; background: var(--paper); }
  .letterhead {
    position: relative;
    width: 942px;
    height: 1200px;
    background: var(--paper);
    font-family: "Tinos", "Times New Roman", serif;
    color: var(--text-body);
  }
  .brand {
    position: absolute;
    left: 74px;
    top: 74px;
    display: flex;
    align-items: center;
    gap: 18px;
  }
  .brand-square {
    width: 64px;
    height: 64px;
    background: var(--brand-blue);
  }
  .brand-name {
    font-family: "Open Sans", Arial, sans-serif;
    font-weight: 400;
    font-size: 34px;
    line-height: 1.05;
    color: var(--brand-blue);
  }
  .brand-name span { display: block; font-size: 17px; letter-spacing: 3.4px; text-transform: uppercase; }
  .meta {
    position: absolute;
    left: 127px;
    top: 352px;
    font-size: 12.5px;
    line-height: 24px;
    color: var(--text-dark);
  }
  .meta strong { font-weight: 700; }
  .letter-body {
    position: absolute;
    left: 127px;
    top: 426px;
    width: 732px;
    font-size: 11.6px;
    line-height: 24px;
    text-align: justify;
  }
  .letter-body p { margin-bottom: 29px; }
  .letter-body .salutation { margin-bottom: 0; }
  .corner-band {
    position: absolute;
    left: 0;
    bottom: 0;
    width: 113px;
    height: 388px;
    background: var(--pale-blue);
  }
  .sign-off {
    position: absolute;
    left: 127px;
    top: 828px;
    font-size: 12px;
    line-height: 18px;
    color: var(--text-dark);
  }
  .sign-off .sign-name { text-transform: uppercase; }
  .signature {
    position: absolute;
    left: 127px;
    top: 890px;
    width: 250px;
    height: 120px;
    background: linear-gradient(135deg, #f1f1f1, #e2e2e2);
  }
  .contact {
    position: absolute;
    left: 700px;
    top: 1082px;
    display: flex;
    gap: 12px;
    font-family: "Open Sans", Arial, sans-serif;
    font-size: 12px;
    color: var(--text-dark);
  }
  .contact-icons {
    display: flex;
    flex-direction: column;
    gap: 0;
    padding-right: 10px;
    border-right: 1.5px solid var(--accent-turquoise);
  }
  .contact-icons svg { width: 14px; height: 17.8px; display: block; fill: var(--accent-turquoise); }
  .contact-lines li { list-style: none; line-height: 17.8px; }
  .contact-icons .gap { height: 17.8px; }
</style>
</head>
<body>
<main class="letterhead">
  <header class="brand">
    <div class="brand-square"></div>
    <div class="brand-name">TalkWell<span>Consultants</span></div>
  </header>

  <section class="meta">
    <p><strong>Data :</strong> Mon , 25 / 3 / 2013</p>
    <p><strong>Recipient :</strong> Mr. Alan Reed Hartley</p>
  </section>

  <section class="letter-body">
    <p class="salutation">Dear Mr. Alan Reed</p>
    <p>Lorem ipsum dolor sit amet, consectetur adipiscing elit. Praesent vulputate, neque ac accumsan suscipit, justo turpis volutpat nisl, tempus fermentum eros tortor et elit. Vivamus porttitor faucibus gravida. Quisque pharetra gravida luctus. Donec eget turpis libero. Ut ac dolor urna, quis tempor nunc. Donec vitae mauris purus, euismod eleifend nulla. Lorem ipsum dolor sit amet, consectetur adipiscing elit. Donec ut purus tellus. Aenean quis dignissim lacus. Vestibulum suscipit vehicula cursus. Suspendisse potenti. Ut in sem nisi. Sed et massa leo.</p>
    <p>Fusce varius libero vel risus condimentum suscipit. Nullam tristique ultrices massa a volutpat. Donec sed dictum metus. Curabitur fringilla nibh eu ligula pharetra a interdum quam aliquam. Maecenas aliquam elit eu orci rutrum molestie. Proin nisl justo, varius a volutpat nec, ultricies sed sem. Nam sit amet imperdiet sem. Phasellus vitae mauris odio. Etiam in purus dui. Etiam ultricies, ante vel iaculis sodales, arcu leo adipiscing leo, sit amet mollis dui nisi non quam.</p>
    <p>Suspendisse sagittis laoreet dolor, vitae rhoncus arcu volutpat quis. Vestibulum at placerat dolor. Vivamus eu lacus ut enim molestie consectetur. Quisque ac lorem vel orci sagittis sollicitudin. Nunc ut quam sem, quis volutpat libero. Cum sociis natoque penatibus et magnis dis parturient montes, nascetur ridiculus mus. Vestibulum ante ipsum primis in faucibus orci luctus et ultrices posuere cubilia Curae; Donec tempor velit in velit feugiat sit amet vulputate nisl posuere..</p>
  </section>

  <div class="corner-band"></div>

  <section class="sign-off">
    <p class="sign-name">Alan Reed</p>
    <p>General director</p>
  </section>
  <div class="signature" role="img" aria-label="Handwritten signature of the general director"></div>

  <footer class="contact">
    <div class="contact-icons">
      <svg viewBox="0 0 14 18" aria-hidden="true"><path d="M7 2a4.5 4.5 0 0 0-4.5 4.5C2.5 10 7 15 7 15s4.5-5 4.5-8.5A4.5 4.5 0 0 0 7 2zm0 6.2a1.8 1.8 0 1 1 0-3.6 1.8 1.8 0 0 1 0 3.6z"/></svg>
      <div class="gap"></div>
      <svg viewBox="0 0 14 18" aria-hidden="true"><path d="M2 6c0-1.5 2.2-2.5 5-2.5S12 4.5 12 6v1.2H9.6V5.9H4.4v1.3H2zM3.5 8h7l1 6h-9zm3.5 1.6a1.9 1.9 0 1 0 0 3.8 1.9 1.9 0 0 0 0-3.8z"/></svg>
      <svg viewBox="0 0 14 18" aria-hidden="true"><path d="M1.5 5h11v8h-11zm1 1 4.5 3.4L11.5 6z"/></svg>
      <svg viewBox="0 0 14 18" aria-hidden="true"><path d="M7 3.5a5.5 5.5 0 1 0 0 11 5.5 5.5 0 0 0 0-11zm-4.3 5h2.1c0-1.3.3-2.4.7-3.3a4.4 4.4 0 0 0-2.8 3.3zm0 1a4.4 4.4 0 0 0 2.8 3.3c-.4-.9-.7-2-.7-3.3zm3.1 0c0 1.5.5 2.9 1.2 3.7.7-.8 1.2-2.2 1.2-3.7zm0-1h2.4C8.2 7 7.7 5.6 7 4.8 6.3 5.6 5.8 7 5.8 8.5zm3.4 0h2.1a4.4 4.4 0 0 0-2.8-3.3c.4.9.7 2 .7 3.3zm0 1c0 1.3-.3 2.4-.7 3.3a4.4 4.4 0 0 0 2.8-3.3z"/></svg>
    </div>
    <ul class="contact-lines">
      <li>48 Meadow Lane</li>
      <li>Lakeside, 40512</li>
      <li>555 019 2846</li>
      <li>info@talkwell.com</li>
      <li>www.talkwell.com</li>
    </ul>
  </footer>
</main>
</body>
</html>
```